Bramblewood Coatings of Central Florida, LLC. Start-up painting business needs a professional web desig

We have a start up painting business that would like to reach/focus on commercial clients like building contractors, HOA's, apartment complexes, etc.. We would like a residential aspect to the web design as well. We have an existing website at "trybramblewoodcoats.com" with usable content. Have logo and color scheme attached. Use provided website ONLY as template. Add commercial services page. Can type own content when needed.

Industry/Entity Type

Apartment

Number of Pages Required

5+ page

Font styles to use
Serif
Sans Serif
Decorative
Script

Requirements
Must have
• Commercial services

```html
<!DOCTYPE html>
<html lang="en">
<head>
<meta charset="utf-8">
<title>Bramblewood Coatings</title>
<link href="https://fonts.googleapis.com/css2?family=Ubuntu:wght@400;500;700&display=swap" rel="stylesheet">
<style>
:root{
  --olive-light:#8e8851;
  --olive:#777140;
  --olive-dark:#5f5a2f;
  --heading:#6b6536;
  --brand-red:#e3261c;
  --phone-blue:#2b9fd8;
  --page-grey:#ececec;
  --panel-border:#e2e2e2;
  --text:#555;
  --text-light:#777;
  --green:#4cc21a;
  --blue:#1c52f0;
  --orange:#f5a30c;
  --red:#ee1c1c;
}
*{margin:0;padding:0;box-sizing:border-box}
html,body{width:822px;height:1200px;overflow:hidden}
body{position:relative;font-family:"Ubuntu",sans-serif;color:var(--text);
  background:linear-gradient(to bottom,#fff 0,#fff 346px,var(--page-grey) 346px)}
.abs{position:absolute}

/* navigation */
.main-nav{left:0;top:0;width:822px;height:50px;
  background:linear-gradient(to bottom,var(--olive-light),var(--olive))}
.main-nav a{position:absolute;top:0;height:50px;line-height:50px;text-align:center;
  color:#fff;font-size:12px;text-decoration:none;letter-spacing:-.3px;
  border-right:1px solid rgba(255,255,255,.18)}
.main-nav a.current{background:rgba(0,0,0,.14)}
.search-icon{left:742px;top:18px}

/* header */
.brand-mark{left:74px;top:72px;width:50px;height:50px;background:#d9cbbb}
.brand-name{left:152px;top:84px;font-size:23px;font-weight:500;color:var(--brand-red);letter-spacing:-.6px}
.phones{right:66px;top:75px;text-align:right;color:var(--phone-blue);font-size:18px;line-height:24px;letter-spacing:-.2px}
.phone-dot{display:inline-block;width:11px;height:11px;border-radius:50%;background:var(--phone-blue);margin-right:8px;vertical-align:1px}

/* content panel */
.content-panel{left:67px;top:149px;width:688px;height:968px;background:#fff;border:1px solid var(--panel-border)}

.hero{left:83px;top:166px;width:656px;height:272px;
  background:linear-gradient(100deg,#e4e4e2,#d6c4a8)}
.hero-caption{left:83px;top:378px;width:656px;height:60px;background:rgba(70,70,70,.78)}
.hero-caption h2{position:absolute;left:19px;top:17px;font-weight:500;font-size:22px;letter-spacing:-.8px;color:#fff}
.hero-dots{position:absolute;right:20px;top:26px;display:flex;gap:7px}
.hero-dots i{width:8px;height:8px;border-radius:50%;background:#9a9a9a}
.hero-dots i.on{background:#fff}

.service{width:320px;height:188px;background:linear-gradient(to bottom,#fff,#eeeeee)}
.service-label{position:absolute;top:14px;width:180px;height:46px;color:#fff;
  font-size:13.5px;font-weight:500;letter-spacing:-.4px;line-height:46px;padding-left:10px}
.service p{position:absolute;left:21px;top:80px;width:285px;font-size:8.6px;line-height:14px;color:var(--text-light)}
.btn-dark{position:absolute;left:18px;top:121px;width:72px;height:36px;border-radius:4px;
  background:linear-gradient(to bottom,#3a3a3a,#050505);color:#fff;font-size:10px;line-height:36px;text-align:center}

/* lower section */
.section-title{font-size:20px;font-weight:500;letter-spacing:-.8px;color:var(--heading)}
.photo-frame{width:197px;height:94px;border:3px solid #fff;box-shadow:0 0 0 1px #ddd}
.teaser{width:200px;font-size:8.6px;line-height:14px;color:var(--text)}
.btn-olive{width:74px;height:26px;border-radius:13px;background:linear-gradient(to bottom,var(--olive-light),var(--olive-dark));
  color:#fff;font-size:10px;line-height:26px;text-align:center;letter-spacing:-.2px}

.quote-box{left:534px;top:858px;width:204px;height:231px;background:#f6f6f6;border:1px solid #ddd}
.quote-box h3{position:absolute;left:15px;top:18px;font-weight:500;font-size:20px;letter-spacing:-.8px;color:var(--heading)}
.field{position:absolute;left:14px;width:173px;background:#fff;border:1px solid #ddd;font-size:8.5px;color:#555;padding:9px 9px}

/* footer */
.footer-links{left:66px;top:1140px;font-size:10px;color:#888;letter-spacing:-.2px}
.footer-links span{margin:0 6px;color:#aaa}
.copyright{left:67px;top:1163px;font-size:8px;color:#999}
.social{top:1142px;width:14px;height:14px;border-radius:2px}
</style>
</head>
<body>

<nav class="main-nav abs">
  <a class="current" style="left:67px;width:72px">HOME</a>
  <a style="left:139px;width:95px">ABOUT US</a>
  <a style="left:234px;width:94px">SERVICES</a>
  <a style="left:328px;width:93px">PAINTING</a>
  <a style="left:421px;width:107px;border-right:none">CONTACT US</a>
  <svg class="search-icon abs" width="12" height="12" viewBox="0 0 12 12"><circle cx="5" cy="5" r="3.6" fill="none" stroke="#fff" stroke-width="1.6"/><line x1="7.7" y1="7.7" x2="11" y2="11" stroke="#fff" stroke-width="1.8"/></svg>
</nav>

<header>
  <div class="brand-mark abs"></div>
  <div class="brand-name abs">BRAMBLEWOOD COATINGS</div>
  <div class="phones abs"><span class="phone-dot"></span>+1.863-555-0142<br>+1.863-555-0186</div>
</header>

<div class="content-panel abs"></div>

<div class="hero abs" role="img" aria-label="Painter hanging wallpaper in a bright room"></div>
<div class="hero-caption abs">
  <h2>INTERIOR DESIGN SERVICES</h2>
  <div class="hero-dots"><i class="on"></i><i></i><i></i><i></i></div>
</div>

<div class="service abs" style="left:83px;top:448px">
  <div class="service-label" style="left:82px;background:var(--green)" role="img" aria-label="Green paint roller stroke">INTERIOR DESIGN</div>
  <p>Nemo enim ipsam voluptatem quia voluptas sit aspernatur aut odit aut fugit, sed quia consequuntur magni ...</p>
  <div class="btn-dark">Read More</div>
</div>
<div class="service abs" style="left:418px;top:448px">
  <div class="service-label" style="left:23px;background:var(--blue)" role="img" aria-label="Blue paint roller stroke">COMMERCIAL SERVICES</div>
  <p>Nemo enim ipsam voluptatem quia voluptas sit aspernatur aut odit aut fugit, sed quia consequuntur magni ...</p>
  <div class="btn-dark">Read More</div>
</div>
<div class="service abs" style="left:83px;top:636px">
  <div class="service-label" style="left:84px;background:var(--orange)" role="img" aria-label="Orange paint roller stroke">INTERIOR PAINTING</div>
  <p>Nemo enim ipsam voluptatem quia voluptas sit aspernatur aut odit aut fugit, sed quia consequuntur magni ...</p>
  <div class="btn-dark">Read More</div>
</div>
<div class="service abs" style="left:418px;top:636px">
  <div class="service-label" style="left:23px;background:var(--red)" role="img" aria-label="Red paint roller stroke">EXTERIOR PAINTING</div>
  <p>Nemo enim ipsam voluptatem quia voluptas sit aspernatur aut odit aut fugit, sed quia consequuntur magni ...</p>
  <div class="btn-dark">Read More</div>
</div>

<h2 class="section-title abs" style="left:83px;top:854px">ABOUT US</h2>
<div class="photo-frame abs" style="left:83px;top:894px;background:linear-gradient(to bottom,#8fb4d2,#5e8a8e)" role="img" aria-label="Waterfront city skyline"></div>
<p class="teaser abs" style="left:85px;top:1003px">Neque porro quisquam est, qui dolorem ipsum quia dolor sit amet, consectetur, adipisci velit, sed quia non numquam...</p>
<div class="btn-olive abs" style="left:83px;top:1060px">READ MORE</div>

<h2 class="section-title abs" style="left:313px;top:854px">OUR AREA</h2>
<div class="photo-frame abs" style="left:313px;top:894px;background:linear-gradient(to right,#e6e6e2,#d9a184)" role="img" aria-label="Painter rolling paint onto an exterior wall"></div>
<p class="teaser abs" style="left:314px;top:1003px">Neque porro quisquam est, qui dolorem ipsum quia dolor sit amet, consectetur, adipisci velit, sed quia non numquam...</p>
<div class="btn-olive abs" style="left:313px;top:1060px">READ MORE</div>

<form class="quote-box abs">
  <h3>REQUEST QUOTE</h3>
  <div class="field" style="top:54px;height:29px">Name</div>
  <div class="field" style="top:90px;height:29px">Email</div>
  <div class="field" style="top:126px;height:56px">Message</div>
  <div class="btn-olive abs" style="left:13px;top:190px">SUBMIT</div>
</form>

<footer>
  <div class="footer-links abs">HOME<span>|</span>ABOUT US<span>|</span>SERVICES<span>|</span>PAINTING<span>|</span>CONTACT US</div>
  <div class="copyright abs">© 2015 | PRIVACY POLICY</div>
  <div class="social abs" style="left:701px;background:#3b5a9a"></div>
  <div class="social abs" style="left:721px;background:#3ba6dc"></div>
  <div class="social abs" style="left:741px;background:#f08a24"></div>
</footer>

</body>
</html>
```